Green Logistics / Last Mile Delivery Firm needs cool one-page website

FYI - We do have a detailed brief in the uploaded files section below
COMPANY
We recently launched the company Brook Logistics which is a pioneer in urban green logistics and provides zero-emissions last mile delivery services (i.e. delivery of parcels with delivery vans to the doorstep of households) for its logistics and retail clients.
We take on urban parcel delivery for our clients with a 100% electric commercial vehicles fleet, fair and sustainable working conditions for our employees and an unparalleled professional and customer-focused mindset.
WEBSITE
In the detailed brief, we have provided examples to emulate. We need the design + coding of the website. Website needs to be friendly/optimized for and should open swiftly on both Android & iOS.
In general, the website should convey
- green mission of the company
- sustainability (good working conditions, focus on employees)
- customer orientation
- professionalism
DESIGN
In the detailed brief, we have provided designs to emulate.
Color design: we do have a logo which features 2 green colors (one lighter and one darker color tone). However, the colors on the website do not necessarily need to follow these 2 colors exactly as we are able to switch the logo colors.
Imagery: should reflect maybe 50% green/leaf/tree , 25% customer and employee orientation, and 25% logistics (here it's important that it is the last mile delivery, i.e. delivery with delivery vans to the doorstep of households)
Coding

```html
<!DOCTYPE html>
<html lang="en">
<head>
<meta charset="utf-8">
<title>Brook Logistics – Sustainable Last Mile</title>
<link href="https://fonts.googleapis.com/css2?family=Oswald:wght@400;500&family=Open+Sans:wght@400;600;700&display=swap" rel="stylesheet">
<style>
:root{
  --green:#3aa935;
  --green-dark:#23861f;
  --green-light:#5cc14a;
  --leaf-pale:#e6f3e2;
  --ink:#222;
  --text:#555;
  --muted:#777;
  --page:#f4f4f4;
  --white:#fff;
  --line:#d8d8d8;
  --red:#e0452c;
}
*{box-sizing:border-box;margin:0;padding:0}
html,body{width:1200px;height:5286px;overflow:hidden}
body{position:relative;background:var(--page);font-family:"Open Sans",sans-serif;color:var(--text)}
.abs{position:absolute}
.heading{font-family:"Oswald",sans-serif;font-weight:500;color:var(--ink);font-size:38px;letter-spacing:-.5px;text-transform:uppercase;line-height:1}
.heading.center{left:0;width:1200px;text-align:center}
.rule{position:absolute;left:584px;width:32px;height:3px;background:var(--green)}
.btn{position:absolute;background:var(--green);color:var(--white);font-weight:700;font-size:14px;text-transform:uppercase;border-radius:24px;display:flex;align-items:center;justify-content:center;text-decoration:none}

/* hero */
.hero{position:absolute;left:0;top:0;width:1200px;height:615px;background:linear-gradient(180deg,#7fa6c9 0%,#b8cfdf 38%,#9fb98a 62%,#4f8a33 85%,#2f6b22 100%)}
.hero-van{position:absolute;left:0;top:250px;width:450px;height:280px;border-radius:0 90px 30px 0;background:linear-gradient(180deg,#f1f2f2 0%,#d7dadb 70%,#b5b9ba 100%);opacity:.9}
.brand{position:absolute;left:113px;top:28px;display:flex;align-items:center;gap:12px}
.brand-dot{width:44px;height:44px;border-radius:50%;background:var(--green)}
.brand-name{font-family:"Oswald",sans-serif;font-weight:500;font-size:30px;color:var(--green-light);text-transform:uppercase}
.contact-mini{position:absolute;top:18px;display:flex;align-items:center;gap:8px;color:var(--white)}
.contact-mini .ring{width:30px;height:30px;border:2px solid var(--white);border-radius:50%;display:flex;align-items:center;justify-content:center}
.contact-mini small{display:block;font-size:10px}
.contact-mini b{display:block;font-size:14px;font-weight:600}
.lang{position:absolute;left:989px;top:22px;display:flex;align-items:center;gap:8px;color:var(--white);font-size:12px}
.lang i{width:30px;height:20px;background:#2c3f8a;display:block}
.nav a{position:absolute;top:74px;color:var(--white);font-size:15px;text-decoration:none}
.nav a.active{color:var(--green-light)}
.hero-title{left:657px;top:272px;font-family:"Oswald",sans-serif;font-weight:400;color:var(--white);font-size:40px;line-height:44px;text-transform:uppercase;width:460px}
.hero-sub{left:657px;top:375px;color:var(--white);font-size:19px}
.arrow{position:absolute;top:318px}

/* about */
.lead{position:absolute;text-align:center;font-size:14px;line-height:27px;color:var(--text)}
.card{position:absolute;top:903px;width:315px;height:394px;background:var(--white);border:1px solid #e4e4e4;box-shadow:0 2px 10px rgba(0,0,0,.08);text-align:center}
.card.featured{background:var(--green);border-color:var(--green)}
.card .icon{width:80px;height:80px;border-radius:50%;margin:28px auto 0;background:var(--green);border:4px solid #d9efd6;display:flex;align-items:center;justify-content:center}
.card.featured .icon{background:var(--white);border-color:#9fd698}
.card h3{margin-top:22px;font-size:23px;font-weight:700;color:var(--ink);text-transform:uppercase}
.card.featured h3,.card.featured p{color:var(--white)}
.card p{margin:12px 22px 0;font-size:12px;line-height:24px;text-align:justify;color:var(--muted)}

/* contrast band */
.band{position:absolute;left:0;top:1387px;width:1200px;height:579px;background:linear-gradient(90deg,#3a3c3e 0%,#5c5a52 35%,#6b8aa8 55%,#3d78b8 75%,#3f7fb9 100%)}
.band-city{position:absolute;left:0;top:300px;width:1200px;height:80px;background:linear-gradient(90deg,rgba(40,40,40,.55) 0%,rgba(60,60,60,.4) 45%,rgba(150,170,190,.45) 55%,rgba(170,190,210,.5) 100%)}
.band-ground{position:absolute;left:0;bottom:0;width:1200px;height:200px;background:linear-gradient(90deg,#a07d4c 0%,#8b6d44 45%,#5c9a36 55%,#3e8d28 100%)}
.band-title{left:174px;top:1443px;font-family:"Oswald",sans-serif;font-weight:400;color:var(--white);font-size:38px;text-transform:uppercase}
.band-title-bar{left:165px;top:1440px;width:3px;height:46px;background:var(--white)}
.band-list h4{font-size:14px;font-weight:400;color:var(--white);text-transform:uppercase;margin-bottom:10px}
.band-list.old h4{text-decoration:underline}
.band-list ul{list-style:none}
.band-list li{font-size:14px;color:var(--white);height:34px;display:flex;align-items:center;gap:10px}
.band-list.old li span{text-decoration:line-through}
.band-list li::before{content:"";width:10px;height:10px;border-radius:50%;background:var(--red);flex:none}
.band-list.new li::before{background:var(--green-light)}

/* services */
.service{position:absolute;top:2230px;width:236px;height:270px;background:var(--white);border:1px solid #e4e4e4;box-shadow:0 2px 10px rgba(0,0,0,.08);text-align:center}
.service .badge{width:100px;height:100px;margin:18px auto 0;border-radius:50%;background:radial-gradient(circle,var(--white) 0%,var(--leaf-pale) 55%,#c9d9c5 100%);display:flex;align-items:center;justify-content:center}
.service h3{margin-top:20px;font-size:14px;font-weight:600;color:var(--ink);line-height:20px;padding:0 10px}
.service p{margin-top:8px;font-size:12px;line-height:24px;color:var(--muted);padding:0 18px}

/* cta */
.cta{position:absolute;left:0;top:2585px;width:1200px;height:364px;background:linear-gradient(180deg,#1d3b1b 0%,#2d5a24 45%,#3f7a2c 100%)}
.cta-text{left:113px;top:2768px;width:760px;color:var(--white);font-size:13.5px;line-height:26px}

/* careers */
.photo-careers{left:127px;top:3103px;width:450px;height:297px;background:linear-gradient(100deg,#dfe6ec 0%,#b9c6d1 35%,#3f7fc4 55%,#d8a868 80%,#c99a5c 100%)}
.careers-text{left:599px;top:3110px;width:474px;font-size:13px;line-height:26.5px;text-align:justify;color:var(--text)}
.acc{position:absolute;left:127px;width:946px;border-top:1px solid var(--line);height:82px;display:flex;align-items:center;gap:18px;padding-left:20px;font-size:15px;font-weight:600;color:var(--ink)}
.acc .plus{font-size:22px;font-weight:400}
.acc.last{border-bottom:1px solid var(--line)}

/* contact */
.contact-sub{left:113px;top:3880px;font-size:33px;font-weight:700;color:var(--green)}
.contact-text{left:113px;top:3932px;width:960px;font-size:13px;line-height:28px}
.map{left:0;top:4002px;width:1200px;height:400px;background:linear-gradient(135deg,#e9e6df 0%,#efede6 50%,#e4e9e0 100%)}
.map-card{left:133px;top:4083px;width:226px;height:150px;background:var(--white);box-shadow:0 2px 8px rgba(0,0,0,.2);padding:22px 18px;font-size:12px;color:var(--ink);line-height:18px}
.map-card b{display:block;font-size:15px;color:var(--green);margin-bottom:8px}
.map-pin{left:384px;top:4225px}
.info{position:absolute;left:137px;display:flex;gap:18px}
.info h5{font-size:20px;font-weight:600;color:var(--ink)}
.info p{font-size:12px;font-weight:600;color:var(--text);line-height:20px;margin-top:4px}
.field{position:absolute;background:var(--white);border:1px solid var(--line);font-size:13px;color:var(--muted);padding:12px 10px}

/* footer */
.footer{position:absolute;left:0;top:4781px;width:1200px;height:505px;background:linear-gradient(180deg,var(--page) 0%,#d9e7cf 25%,#8fbe5d 55%,#4c8c2a 80%,#3a7a22 100%)}
.foot-brand{left:0;width:1200px;top:4960px;display:flex;flex-direction:column;align-items:center;gap:10px}
.foot-brand .brand-dot{width:80px;height:80px;background:var(--white)}
.foot-brand span{font-family:"Oswald",sans-serif;font-size:30px;color:var(--white);text-transform:uppercase}
.foot-nav a{position:absolute;top:5127px;color:var(--white);font-size:16px;font-weight:700;text-decoration:none}
.social{position:absolute;top:5182px;width:36px;height:36px;border-radius:50%;background:var(--green)}
.copyright{left:0;width:1200px;top:5241px;text-align:center;font-size:12px;color:var(--white)}
</style>
</head>
<body>

<!-- HERO -->
<header class="hero" role="img" aria-label="Electric delivery van driving along a green field road under a blue sky">
  <div class="hero-van"></div>
</header>
<div class="brand"><span class="brand-dot"></span><span class="brand-name">Brook Logistics</span></div>
<div class="contact-mini" style="left:592px">
  <span class="ring"><svg width="14" height="14" viewBox="0 0 24 24" fill="#fff"><path d="M6.6 10.8a15 15 0 0 0 6.6 6.6l2.2-2.2c.3-.3.7-.4 1-.2 1.1.4 2.3.6 3.6.6.6 0 1 .4 1 1V20c0 .6-.4 1-1 1A17 17 0 0 1 3 4c0-.6.4-1 1-1h3.5c.6 0 1 .4 1 1 0 1.3.2 2.5.6 3.6.1.3 0 .7-.2 1z"/></svg></span>
  <div><small>Call Now</small><b>555.014.2090</b></div>
</div>
<div class="contact-mini" style="left:756px">
  <span class="ring"><svg width="14" height="14" viewBox="0 0 24 24" fill="none" stroke="#fff" stroke-width="2"><rect x="3" y="5" width="18" height="14"/><path d="M3 6l9 7 9-7"/></svg></span>
  <div><small>Email</small><b>info@brooklogistics.com</b></div>
</div>
<div class="lang"><i></i>English ▾</div>
<nav class="nav">
  <a class="active" style="left:500px">Home</a>
  <a style="left:624px">About</a>
  <a style="left:750px">Services</a>
  <a style="left:889px">Careers</a>
  <a style="left:1026px">Contact</a>
</nav>
<svg class="arrow" style="left:74px" width="20" height="30" viewBox="0 0 20 30"><path d="M16 2 4 15l12 13" stroke="#fff" stroke-width="2" fill="none"/></svg>
<svg class="arrow" style="left:1108px" width="20" height="30" viewBox="0 0 20 30"><path d="M4 2l12 13L4 28" stroke="#fff" stroke-width="2" fill="none"/></svg>
<h1 class="abs hero-title">Brook Logistics – Sustainable last mile</h1>
<p class="abs hero-sub">Because we care about trees!</p>
<a class="btn" style="left:657px;top:425px;width:180px;height:47px">Get started</a>
<svg class="abs" style="left:0;top:520px" width="1200" height="120" viewBox="0 0 1200 120">
  <path d="M0 45 Q600 150 1200 20 L1200 120 L0 120Z" fill="#f4f4f4"/>
  <path d="M0 45 Q600 150 1200 20" stroke="#2e9a2a" stroke-width="5" fill="none"/>
</svg>

<!-- ABOUT -->
<h2 class="heading center abs" style="top:750px">About us</h2>
<span class="rule" style="top:805px"></span>
<p class="lead" style="left:200px;top:822px;width:800px">Lorem ipsum dolor sit amet, consectetur adipiscing elit, sed do eiusmod tempor incidmagna aliqua. Quis ipsum suspendisse ultrices gravida. Risus commodo viverra maecenas accumsan lacus vel facilisis.</p>

<article class="card" style="left:111px">
  <div class="icon"><svg width="34" height="34" viewBox="0 0 24 24" fill="none" stroke="#fff" stroke-width="1.8"><rect x="4" y="3" width="16" height="18" rx="2"/><path d="M8 8h8M8 12h8M8 16h5"/></svg></div>
  <h3>Who we are</h3>
  <p>Brook Logistics is a pioneer in urban green logistics and provides zero-emissions last mile delivery services for its logistics and retail clients. We take on urban parcel delivery for our clients with a 100% electric commercial vehicles fleet, fair and sustainable working conditions for our employees and an unparalleled professional and customer-focused mindset.</p>
</article>
<article class="card featured" style="left:441px">
  <div class="icon"><svg width="34" height="34" viewBox="0 0 24 24" fill="none" stroke="#3aa935" stroke-width="1.8"><circle cx="12" cy="12" r="9"/><circle cx="12" cy="12" r="5"/><circle cx="12" cy="12" r="1.5" fill="#3aa935"/></svg></div>
  <h3>Our mission</h3>
  <p>To satisfy consumers' ever-rising desire to buy products online, the CO2 emissions from delivery traffic will increase by 32% in the top 100 cities globally until 2030. Our clients care about our planet the same way we do, which is why Brook Logistics helps to make the planet a better place by running the most environmentally friendly urban last mile possible.</p>
</article>
<article class="card" style="left:771px">
  <div class="icon"><svg width="34" height="34" viewBox="0 0 24 24" fill="none" stroke="#fff" stroke-width="1.8"><path d="M6 4h12l3 5-9 11L3 9z"/><path d="M3 9h18M9 4l3 16 3-16"/></svg></div>
  <h3>Our values</h3>
  <p>We see ourselves as a professional services company who strongly cares about the environment, its clients and their customers, as well as its employees. We believe that delivering parcels with zero emissions and providing a unique customer experience through a highly professional attitude and a great team spirit are the cornerstones for Brook Logistics to operate in today's world in a sustainable yet profitable way.</p>
</article>

<!-- CONTRAST BAND -->
<section class="band" role="img" aria-label="Polluted grey city under storm clouds on the left, clean green city under blue sky on the right">
  <div class="band-city"></div>
  <div class="band-ground"></div>
</section>
<span class="abs band-title-bar"></span>
<h2 class="abs band-title">Brook Logistics is...</h2>
<div class="abs band-list old" style="left:257px;top:1537px">
  <h4>An ordinary parcel delivery firm</h4>
  <ul>
    <li><span>Polluting our cities</span></li>
    <li><span>Always in a rush</span></li>
    <li><span>Short-term oriented</span></li>
    <li><span>Focusing on profit only</span></li>
    <li><span>Yet another parcel delivery firm</span></li>
  </ul>
</div>
<div class="abs band-list new" style="left:630px;top:1537px">
  <h4>A pioneering green last mile</h4>
  <ul>
    <li>Delivering parcels emissions-free</li>
    <li>Putting customer experience first</li>
    <li>Operating the business sustainably</li>
    <li>Focusing on the environment, customers and employees</li>
    <li>A professional services company</li>
  </ul>
</div>

<!-- SERVICES -->
<h2 class="heading center abs" style="top:2047px">Our services</h2>
<span class="rule" style="top:2100px"></span>
<p class="lead" style="left:200px;top:2120px;width:800px">Brook Logistics provides last mile delivery services in urban areas to clients in the logistics and retail space. Our permanent employees are all highly trained and commit to highest professional standards which we continuously review and further develop with them.</p>

<div class="service" style="left:111px">
  <div class="badge"><svg width="44" height="44" viewBox="0 0 24 24" fill="none" stroke="#3aa935" stroke-width="1.6"><path d="M5 19C5 10 11 5 20 4c0 9-5 15-13 15z"/><path d="M5 19l9-9"/></svg></div>
  <h3>Zero-emission delivery</h3><p>We live a customer-oriented mindset, always measuring ourselves against their experience</p></div>
<div class="service" style="left:357px">
  <div class="badge"><svg width="44" height="44" viewBox="0 0 24 24" fill="none" stroke="#3aa935" stroke-width="1.6"><rect x="3" y="8" width="12" height="9"/><path d="M15 11h4l2 3v3h-6"/><circle cx="7" cy="18" r="2" fill="#fff"/><circle cx="17" cy="18" r="2" fill="#fff"/></svg></div>
  <h3>Highly trained delivery drivers</h3><p>We only employ permanently, train far above average, and live a great team spirit</p></div>
<div class="service" style="left:605px">
  <div class="badge"><svg width="44" height="44" viewBox="0 0 24 24" fill="none" stroke="#3aa935" stroke-width="1.6"><circle cx="12" cy="12" r="9"/><path d="M3 12h18M12 3c3 3 3 15 0 18M12 3c-3 3-3 15 0 18"/></svg></div>
  <h3>Professional all around</h3><p>We honor our commitments and hold ourselves to the highest professional standards</p></div>
<div class="service" style="left:852px">
  <div class="badge"><svg width="44" height="44" viewBox="0 0 24 24" fill="none" stroke="#3aa935" stroke-width="1.6"><circle cx="8" cy="8" r="3"/><circle cx="16" cy="8" r="3"/><path d="M2 20c0-4 3-6 6-6s6 2 6 6M10 20c0-4 3-6 6-6s6 2 6 6"/></svg></div>
  <h3>Unparalleled customer focus</h3><p>We live a customer-oriented mindset, always measuring ourselves against their experience</p></div>

<!-- CTA -->
<section class="cta" role="img" aria-label="Aerial view of a dense green forest"></section>
<h2 class="heading abs" style="left:113px;top:2705px;color:#fff">Get in touch with Brook Logistics</h2>
<p class="abs cta-text">If you got excited, or have a question about our services, our approach, our jobs or just want to get in touch to chat about how green logistics can make the planet a little bit better, please get in touch!</p>
<a class="btn" style="left:905px;top:2763px;width:180px;height:48px">Contact us</a>

<!-- CAREERS -->
<h2 class="heading center abs" style="top:3012px">Careers</h2>
<span class="rule" style="top:3066px"></span>
<div class="abs photo-careers" role="img" aria-label="Smiling delivery driver holding a parcel beside an open van"></div>
<p class="abs careers-text">If you join Brook Logistics, you join a family. We elevate one another, care for each other's wellbeing and growth, and celebrate our successes. We strongly believe growth is a team sport and that every member of the family fully contributes to the achievements of the company overall. At the heart of everything we do at Brook Logistics is a relentless focus on our mission. That's why we aim to ensure our employees can follow their own passion at the workplace, be this working in a truly collaborative and caring team, putting a smile on a customer's face or making the world a better place. While we are helping our clients grow by delivering their parcels, we are also helping all our employees</p>

<div class="acc" style="top:3427px;height:88px"><span class="plus">+</span>Full-time driver / parcel deliverer (m/f/d) for Berlin</div>
<div class="acc" style="top:3515px"><span class="plus">+</span>Your tasks as a delivery driver:</div>
<div class="acc" style="top:3597px"><span class="plus">+</span>Required knowledge and skills</div>
<div class="acc last" style="top:3679px;height:80px"><span class="plus">+</span>What you can expected from the Brook Logistics family:</div>

<!-- CONTACT -->
<h2 class="heading abs" style="left:113px;top:3836px">Contact</h2>
<p class="abs contact-sub">We'd love to hear from you!</p>
<p class="abs contact-text">Whether you have a question about our services, our approach, our jobs or just want to get in touch to chat about how green logistics can make the planet a little bit better, our team is ready to answer your questions and enquiries.</p>

<div class="abs map" role="img" aria-label="Street map of the city centre around the office"></div>
<div class="abs map-card"><b>Brook Logistics</b>48 Greenway Lane Springdale<br>40210</div>
<svg class="abs map-pin" width="24" height="34" viewBox="0 0 24 34"><path d="M12 0C5 0 0 5 0 12c0 9 12 22 12 22s12-13 12-22C24 5 19 0 12 0z" fill="#e0452c"/><circle cx="12" cy="12" r="4" fill="#fff"/></svg>

<div class="info" style="top:4443px">
  <svg width="28" height="32" viewBox="0 0 24 28" fill="none" stroke="#3aa935" stroke-width="2"><path d="M12 26s9-9 9-15a9 9 0 0 0-18 0c0 6 9 15 9 15z"/><circle cx="12" cy="11" r="3"/></svg>
  <div><h5>Location:</h5><p>48 Greenway Lane Springdale<br>40210</p></div>
</div>
<div class="info" style="top:4531px">
  <svg width="34" height="26" viewBox="0 0 26 20" fill="none" stroke="#3aa935" stroke-width="2"><rect x="1" y="1" width="24" height="18"/><path d="M1 2l12 9 12-9"/></svg>
  <div><h5>Email:</h5><p>info@brooklogistics.com</p></div>
</div>
<div class="info" style="top:4601px">
  <svg width="30" height="30" viewBox="0 0 24 24" fill="none" stroke="#3aa935" stroke-width="2"><path d="M6.6 10.8a15 15 0 0 0 6.6 6.6l2.2-2.2c.3-.3.7-.4 1-.2 1.1.4 2.3.6 3.6.6.6 0 1 .4 1 1V20c0 .6-.4 1-1 1A17 17 0 0 1 3 4c0-.6.4-1 1-1h3.5c.6 0 1 .4 1 1 0 1.3.2 2.5.6 3.6.1.3 0 .7-.2 1z"/></svg>
  <div><h5>Call:</h5><p>555 - 014 - 2090</p></div>
</div>

<div class="field" style="left:478px;top:4443px;width:287px;height:47px">Your Name</div>
<div class="field" style="left:776px;top:4443px;width:287px;height:47px">Your Email</div>
<div class="field" style="left:478px;top:4500px;width:585px;height:48px">Subject</div>
<div class="field" style="left:478px;top:4557px;width:585px;height:103px">Message</div>
<a class="btn" style="left:685px;top:4681px;width:169px;height:45px">Send message</a>

<!-- FOOTER -->
<footer class="footer" role="img" aria-label="Close-up of fresh green grass in morning light"></footer>
<div class="abs foot-brand"><span class="brand-dot"></span><span>Brook Logistics</span></div>
<nav class="foot-nav">
  <a style="left:313px">HOME</a>
  <a style="left:423px">ABOUT</a>
  <a style="left:545px">SERVICES</a>
  <a style="left:677px">CAREERS</a>
  <a style="left:809px">CONTACT</a>
</nav>
<span class="social" style="left:530px"></span>
<span class="social" style="left:582px"></span>
<span class="social" style="left:634px"></span>
<p class="abs copyright">© 2020 Brook Logistics &nbsp; | &nbsp; Legal Notice &nbsp; | &nbsp; Privacy Policy</p>

</body>
</html>
```